Powerpoint design for management consultant

We need a powerpoint design to use for our corporate presentations, proposal summaries and for delivering report recommendations.

Target Market(s)

Executives in Government & Private Industry

Industry/Entity Type

Consultant

Requirements
Must have
• Must use the company logo contained in the uploaded files.
Must be a powerpoint template file (.potx) that can be used with Powerpoint 2007 and later.
Must have a title slide.
Must have a purpose slide (in today's presentation we will cover ....)
Must have an agenda slide.
Must have three topic slides (topic1, topic2, topic3) as transition slides
Must support side by side comparisons
Any images used must be available royalty/ license free
Must have a summary slide.
Must have a questions slide at the end.
Must have a footer containing slide number in format of x of y.
Must have a footer containing presentation name.
Must have a footer containing the presentation date.
Must have a footer containing "confidential"
Nice to have
• The powerpoint should support the ability to represent data using infographics.
Should not have
• no tag lines or references to being management consultants. must not use custom fonts.

```html
<!DOCTYPE html>
<html lang="en">
<head>
<meta charset="utf-8">
<title>Questions slide</title>
<link rel="stylesheet" href="https://fonts.googleapis.com/css2?family=Carlito:wght@400;700&display=swap">
<style>
  :root {
    --slide-bg: #ffffff;
    --accent-orange: #e36c0a;
    --brand-navy: #2d3e50;
    --footer-grey: #6b6b6b;
    --card-ink: #111111;
    --photo-top: #f1eeec;
    --photo-bottom: #e3dfdd;
  }
  * { margin: 0; padding: 0; box-sizing: border-box; }
  html, body {
    width: 1200px; height: 899px; overflow: hidden;
    background: var(--slide-bg);
    font-family: "Carlito", "Calibri", sans-serif;
  }
  .slide { position: relative; width: 1200px; height: 899px; overflow: hidden; background: var(--slide-bg); }
  .hero-photo {
    position: absolute; left: 0; top: 0; width: 876px; height: 765px;
    background: linear-gradient(160deg, var(--photo-top) 0%, var(--photo-bottom) 100%);
  }
  .card-prompt {
    position: absolute; left: 404px; top: 322px;
    font-size: 56px; font-weight: 400; color: var(--card-ink);
    line-height: 1; transform: rotate(-3deg); letter-spacing: 0.5px;
  }
  .question-mark { position: absolute; left: 0; top: 0; width: 1200px; height: 899px; }
  .slide-footer {
    position: absolute; left: 0; bottom: 0; width: 1200px; height: 90px;
    color: var(--footer-grey);
  }
  .footer-item { position: absolute; top: 50px; font-size: 26px; line-height: 1; }
  .footer-date { left: 13px; }
  .footer-confidential { left: 169px; }
  .footer-title { left: 372px; }
  .brand-name {
    position: absolute; left: 806px; top: 13px;
    font-size: 78px; font-weight: 700; color: var(--brand-navy);
    letter-spacing: 4px; line-height: 1;
  }
  .slide-number { position: absolute; left: 1150px; top: 47px; font-size: 31px; line-height: 1; color: var(--footer-grey); }
</style>
</head>
<body>
  <main class="slide">
    <div class="hero-photo" role="img" aria-label="Photo of a hand holding up a blank white card"></div>
    <p class="card-prompt">Questions?</p>

    <svg class="question-mark" viewBox="0 0 910 683" aria-hidden="true">
      <path d="M655 12 C720 -38 882 -22 886 100 C890 190 792 232 767 300 C752 345 752 400 756 436"
            fill="none" stroke="var(--accent-orange)" stroke-width="54"/>
      <circle cx="787" cy="541" r="42" fill="var(--accent-orange)"/>
    </svg>

    <footer class="slide-footer">
      <span class="footer-item footer-date">23-Oct-13</span>
      <span class="footer-item footer-confidential">Confidential</span>
      <span class="footer-item footer-title">Presentation name</span>
      <span class="brand-name">NORVALT</span>
      <span class="slide-number">24</span>
    </footer>
  </main>
</body>
</html>
```